New profile page for existing party website

For the party website 'Revelmap' we need a new design for the user profile page.

The page should show
* a profile picture
* basic information like name, age and city
* music styles he/she likes
* links to their Chatterly profile and website
* a bio (HTML content)
* events they plan to go to
* past events
* pictures

Challenge is that some users may have little information (just their name) while others have a huge description, lots of foto's, events, etc.

Please visit http://www.revelmap.example and http://www.revelmap.example/users/gordon

Target Market(s)

Men and women between 18 and 35

Industry/Entity Type

Night Club

Number of Pages Required

2 page

Font styles to use
Other font styles liked:
• Roboto

Requirements
Must have
• Please design how the page looks with a fully filled out profile and with an empty profile.
• It should fit well with the existing website.
• Include designs for both for small screens (mobile) and large screens (tablet, desktop).
Nice to have
• UX design on how to collapse or paginate sections.
• Interactive effects would be a bonus.
Should not have
• The page should not have subnavigation like menus or tabs.

```html
<!DOCTYPE html>
<html lang="nl">
<head>
<meta charset="utf-8">
<title>KaiM Photography – Revelmap</title>
<link href="https://fonts.googleapis.com/css2?family=Open+Sans:wght@400;600;700&family=Raleway:wght@400;500&display=swap" rel="stylesheet">
<style>
:root{
  --black:#000;
  --orange:#f7941d;
  --orange-light:#fbb447;
  --accent:#e88a12;
  --text:#555;
  --heading:#222;
  --rule:#cfcfcf;
  --dark:#2b2b2b;
  --light:#f0f0f0;
  --white:#fff;
}
*{box-sizing:border-box;margin:0;padding:0}
html,body{width:1200px;height:2723px;overflow:hidden}
body{font-family:'Open Sans',sans-serif;color:var(--text);background:var(--white);position:relative}
.wrap{position:relative;width:984px;margin-left:109px}

.site-header{height:116px;background:var(--black);position:relative}
.brand{position:absolute;left:105px;top:36px;color:var(--white);font-family:'Open Sans',sans-serif;font-weight:700;font-size:38px;letter-spacing:-.5px}
.main-nav{position:absolute;left:385px;top:47px;display:flex;gap:25px}
.main-nav a{color:var(--white);text-decoration:none;font-family:'Raleway',sans-serif;font-size:17px;font-weight:500}
.search{position:absolute;left:806px;top:42px;width:162px;height:34px;background:#ececec;border:none;color:#999;font-size:14px;padding:0 14px;line-height:34px}
.account-btn{position:absolute;left:978px;top:40px;width:108px;height:37px;border:2px solid var(--white);color:var(--white);font-size:13px;font-weight:600;text-align:center;line-height:33px}

.profile-hero{height:320px;background:linear-gradient(115deg,var(--orange) 0%,var(--orange-light) 55%,var(--orange) 100%);position:relative;overflow:hidden}
.profile-hero svg.rays{position:absolute;inset:0}
.avatar{position:absolute;left:119px;top:43px;width:220px;height:220px;border-radius:50%;border:4px solid var(--white);background:radial-gradient(circle at 50% 40%,#d9c6b4,#8b6b55 60%,#4a3a30);}
.profile-name{position:absolute;left:358px;top:62px;color:var(--white);font-family:'Raleway',sans-serif;font-size:31px;font-weight:400}
.meta{position:absolute;color:var(--white);font-size:15px;line-height:22px}
.social{position:absolute;top:312px;display:flex;gap:12px;left:358px}
.social span{width:44px;height:44px;border-radius:50%;background:var(--white);display:flex;align-items:center;justify-content:center}

.bio h2,.section-title{font-family:'Raleway',sans-serif;font-weight:400;color:var(--heading);font-size:26px}
.bio-block{padding:0 0 26px}
.bio p,.bio li{font-size:13.5px;line-height:24px}
.bio h2{margin-bottom:10px}
.bio hr{border:none;border-top:1px solid var(--rule);margin:0 0 44px 6px}
.bio ul{list-style:none}
.bio li{padding-left:24px;position:relative;margin-bottom:8px}
.bio li::before{content:"";position:absolute;left:4px;top:8px;width:7px;height:7px;border-right:1.5px solid #777;border-bottom:1.5px solid #777;transform:rotate(-45deg)}

.plans{position:absolute;top:1385px;left:0;width:1200px;height:443px;background:var(--dark)}
.plans .section-title{color:var(--white);position:absolute;left:116px;top:58px;font-size:28px}
.arrows{position:absolute;left:1017px;top:1456px;display:flex;gap:12px}
.arrows span{width:28px;height:28px;border-radius:50%;background:#111;display:flex;align-items:center;justify-content:center}
.event-card{position:absolute;top:118px;width:229px}
.event-card .poster{height:163px;border:3px solid var(--white)}
.event-card h3{color:var(--orange);font-size:20px;font-weight:600;margin:14px 0 2px;font-family:'Open Sans',sans-serif}
.event-card p{color:#ccc;font-size:12.5px;line-height:18px}

.past{position:absolute;top:1828px;left:0;width:1200px;height:323px;background:var(--light);border-bottom:1px solid #ddd}
.past .section-title{position:absolute;left:111px;top:59px;font-size:28px}
.past-item{position:absolute;top:122px;width:310px}
.past-item h4{font-size:14px;font-weight:400;color:#222;margin-bottom:14px}
.past-item p{font-size:13px;line-height:24px;color:#444}
.past-item time{display:block;color:var(--accent);font-size:13px;font-weight:600;margin-top:4px}

.photos{position:absolute;top:2151px;left:0;width:1200px;height:445px}
.photos .section-title{position:absolute;left:107px;top:40px;color:var(--orange);font-size:28px}
.thumb{position:absolute;border:3px solid var(--white);box-shadow:0 0 0 1px #ddd}

.site-footer{position:absolute;top:2596px;left:0;width:1200px;height:127px;background:#111;text-align:center}
.site-footer nav{padding-top:35px;display:flex;justify-content:center;gap:30px}
.site-footer a{color:var(--white);text-decoration:none;font-size:15px}
.site-footer small{display:block;color:#888;font-size:12px;margin-top:12px}
</style>
</head>
<body>
<header class="site-header">
  <div class="brand">Revelmap</div>
  <nav class="main-nav">
    <a href="#">Home</a><a href="#">Agenda</a><a href="#">Free tickets</a><a href="#">Photos</a><a href="#">News</a>
  </nav>
  <div class="search">Zoeken</div>
  <div class="account-btn">My Account</div>
</header>

<section class="profile-hero">
  <svg class="rays" width="1200" height="320" viewBox="0 0 1200 320" aria-hidden="true">
    <polygon points="420,0 760,0 560,320 300,320" fill="#fff" opacity=".08"/>
    <polygon points="820,0 1000,0 900,320 700,320" fill="#fff" opacity=".07"/>
    <polygon points="1050,0 1200,0 1200,200" fill="#fff" opacity=".06"/>
  </svg>
  <div class="avatar" role="img" aria-label="Profile photo of the photographer"></div>
  <h1 class="profile-name">KaiM Photography</h1>
  <div class="meta" style="left:358px;top:114px">Member since: jan 2006</div>
  <div class="meta" style="left:608px;top:114px">Age: 34</div>
  <div class="meta" style="left:721px;top:114px">City: San Francisco</div>
  <div class="meta" style="left:898px;top:114px">Shoots: 500 and counting</div>
  <div class="meta" style="left:358px;top:154px">Music Style Like: Latin / Salsa</div>
  <div class="meta" style="left:608px;top:154px;width:440px">Function: Head promotions, photograper, communication, marketing, and sales.</div>
  <div class="social" style="top:196px">
    <span aria-label="Chatterly"><svg width="20" height="20" viewBox="0 0 20 20"><path d="M3 4h14v9H8l-4 3v-3H3z" fill="var(--orange)"/></svg></span>
    <span aria-label="E-mail"><svg width="20" height="16" viewBox="0 0 20 16"><rect x="1" y="2" width="18" height="12" fill="var(--orange)"/><path d="M1 2l9 7 9-7" stroke="#fff" stroke-width="1.6" fill="none"/></svg></span>
  </div>
</section>

<main class="bio wrap" style="padding-top:50px">
  <div class="bio-block">
    <h2>Wil jij fotograferen voor Revelmap?</h2>
    <p>Als je uitgaan leuk vindt, makkelijk bent in de omgang en uiteraard houdt van fotograferen, biedt Revelmap je de kans een kijkje te nemen in de wereld van de partyfotografie. Door de inzet van de fotografen is Revelmap uitgegroeid tot een van de meest toonaangevende partysites van Nederland. De betrouwbaarheid, de hoge kwaliteit van de foto's en het coveren van de belangrijkste evenementen maakt van Revelmap een van de best bezochte websites in ons vakgebied</p>
  </div>
  <hr>
  <div class="bio-block">
    <h2>Belangrijk informatie</h2>
    <p>Fotograferen voor Revelmap is op vrijwillige basis. Je kan kiezen waar en wanneer je uitgaat en foto's maakt, maar een vaste inbreng word wel van je verwacht. Hoe meer je voor Revelmap doet, hoe meer ervaring je opdoet met de camera en hoe beter je word. Hierdoor kan je weer naar interessantere feesten en festivals. Wat je wel krijgt is gratis entree voor een evenement en soms ook andere voordelen zoals gratis drankjes... Je gaat meestal met ze tweetjes op pad en ontmoet veel nieuwe mensen zoals DJ's en organisatoren. Hoe meer je voor Revelmap werkt hoe meer ervaring je er ook uit zal halen. De beste fotografen doen de leukste en de meest uitdagende evenementen bijvoorbeeld: Solstice Hall, Wildfield Outdoor, Sunrise weekend, Pier Dance etc.</p>
  </div>
  <hr>
  <div class="bio-block">
    <h2>Voorwaarden</h2>
    <ul>
      <li>Je moet 18 jaar of ouder zijn.</li>
      <li>Je moet het aankunnen om hoge kwaliteit foto's te maken en professioneel gedrag vertonen.</li>
      <li>Je moet sociaal zijn; een open persoon zijn die ervan houdt om ander e mensen te ontmoeten.</li>
      <li>Het is een vereiste dat je een digitale spiegelreflex-camera hebt en lichtsterke lens met vast diafragma van F2.8 en natuurlijk een externe flitser (E-TTL).</li>
      <li>Je bent verantwoordelijk voor je eigen vervoer om naar de evenementen te gaan waar je foto's maakt.</li>
    </ul>
  </div>
  <hr>
  <div class="bio-block">
    <h2>Aanmelden</h2>
    <p>Wil jij ook het team van Revelmap versterken en het nachtleven van een andere kant verkennen? Geef je dan op, stuur een mailtje naar kai@revelmap.example Vermeld daar goed in je naam, leeftijd, woonplaats en het type camera dat je hebt en je ervaring op het gebied van fotograferen.</p>
    <p style="margin-top:8px">Bekijk ons online foto album voor de door mij geschoten foto's. Bekijk al mijn videotube filmpjes via mijn eigen videotube kanaal</p>
    <p style="margin-top:8px">www.videotube.example/user/1982KaiM</p>
  </div>
</main>

<section class="plans">
  <h2 class="section-title">Event Plan to Go</h2>
  <div class="event-card" style="left:114px"><div class="poster" role="img" aria-label="Colourful festival poster" style="background:linear-gradient(135deg,#e7472f,#3ca04a 60%,#f2c21a)"></div><h3>Sis parturient mont</h3><p>nascetur ridiculus mus In iaculis facilisis massa Etiam eu urna Sed porta Suspendisse quam leo</p></div>
  <div class="event-card" style="left:363px"><div class="poster" role="img" aria-label="Mint green festival poster" style="background:linear-gradient(135deg,#8ed6bd,#b5e6d3)"></div><h3>Phasellus pellent</h3><p>nascetur ridiculus mus In iaculis facilisis massa Etiam eu urna Sed porta Suspendisse quam leo</p></div>
  <div class="event-card" style="left:610px"><div class="poster" role="img" aria-label="Yellow festival badge artwork" style="background:radial-gradient(circle,#f4d21c 45%,#fff 47%)"></div><h3>Sed porta Suspendisse</h3><p>nascetur ridiculus mus In iaculis facilisis massa Etiam eu urna Sed porta Suspendisse quam leo</p></div>
  <div class="event-card" style="left:858px"><div class="poster" role="img" aria-label="Tropical festival poster" style="background:linear-gradient(180deg,#f1c232,#2f9b5a 60%,#1f5fa8)"></div><h3>Cras a ante vitae</h3><p>nascetur ridiculus mus In iaculis facilisis massa Etiam eu urna Sed porta Suspendisse quam leo</p></div>
</section>
<div class="arrows" aria-hidden="true">
  <span><svg width="10" height="10" viewBox="0 0 10 10"><path d="M7 1L3 5l4 4" stroke="#fff" stroke-width="1.6" fill="none"/></svg></span>
  <span><svg width="10" height="10" viewBox="0 0 10 10"><path d="M3 1l4 4-4 4" stroke="#fff" stroke-width="1.6" fill="none"/></svg></span>
</div>

<section class="past">
  <h2 class="section-title">Past Events</h2>
  <article class="past-item" style="left:112px"><h4>FESTIVAL SOL NUEVO 2016 , Rotterdam</h4><p>In iaculis facilisis massa Etiam eu urna Sed porta Suspendisse quam leo molestie sed luctus quis feugiat in pede Fusce</p><time>March 26, 2016</time></article>
  <article class="past-item" style="left:454px"><h4>FESTIVAL SOL NUEVO 2016 , Rotterdam</h4><p>In iaculis facilisis massa Etiam eu urna Sed porta Suspendisse quam leo molestie sed luctus quis feugiat in pede Fusce</p><time>March 26, 2016</time></article>
  <article class="past-item" style="left:795px"><h4>FESTIVAL SOL NUEVO 2016 , Rotterdam</h4><p>In iaculis facilisis massa Etiam eu urna Sed porta Suspendisse quam leo molestie sed luctus quis feugiat in pede Fusce</p><time>March 26, 2016</time></article>
</section>

<section class="photos">
  <h2 class="section-title">Photos</h2>
  <div class="thumb" role="img" aria-label="Party crowd in orange outfits" style="left:109px;top:101px;width:385px;height:261px;background:linear-gradient(135deg,#e9e3dc,#c98a4a 50%,#e87722)"></div>
  <div class="thumb" role="img" aria-label="Street party photo" style="left:519px;top:101px;width:176px;height:120px;background:linear-gradient(135deg,#7b4a2e,#e87722)"></div>
  <div class="thumb" role="img" aria-label="Street party photo" style="left:713px;top:101px;width:176px;height:120px;background:linear-gradient(135deg,#9bb0c4,#b75a2a)"></div>
  <div class="thumb" role="img" aria-label="Street party photo" style="left:906px;top:101px;width:176px;height:120px;background:linear-gradient(135deg,#a8b89a,#e87722)"></div>
  <div class="thumb" role="img" aria-label="Party guests photo" style="left:519px;top:238px;width:176px;height:124px;background:linear-gradient(135deg,#d9d2cc,#e87722)"></div>
  <div class="thumb" role="img" aria-label="Party guests photo" style="left:713px;top:238px;width:176px;height:124px;background:linear-gradient(135deg,#2a2420,#6d4a38)"></div>
  <div class="thumb" role="img" aria-label="Party guests photo" style="left:906px;top:238px;width:176px;height:124px;background:linear-gradient(135deg,#c9d6e2,#e87722)"></div>
</section>

<footer class="site-footer">
  <nav><a href="#">CONTACT</a><a href="#">TERMS OF USE</a><a href="#">PRIVACY POLICY</a></nav>
  <small>© 2016 Company Name  All right reserved</small>
</footer>
</body>
</html>
```